7BrightHarbor.com - website redesign

We need to redesign 7BrightHarbor.com.
Here are design specs: https://files.example-share.net/deck/8kfQz2LmWp4RtY6NvB3xHcJd9SaE1uTg0oKiZnMb/view

Here is a video going over the design specs:
https://media.example-vault.net/clip/9Rw3TzQp0LmXk7VbNc2Hd5SfJ-/watch

Target Market(s)

Seattle, WA

Number of Pages Required

2 page

Font styles to use
Serif

Colors

Designer to choose colors to be used in the design.

Requirements
Must have
• Desktop and Mobile Designs
Use colors from their logo....as provided in the design specs document.

Should not have
• Please follow design specs as provided in Google Slides. Must watch the video to understand what's needed.

```html
<!DOCTYPE html>
<html lang="en">
<head>
<meta charset="utf-8">
<title>7 Bright Harbor — Certified E-Recycling</title>
<link rel="stylesheet" href="https://fonts.googleapis.com/css2?family=Merriweather:wght@400;700;900&display=swap">
<style>
:root{
  --green:#1f8c3b;
  --green-dark:#0f5424;
  --green-deep:#0b3d1b;
  --green-light:#4fae3a;
  --green-pale:#dcebd0;
  --ink:#222;
  --muted:#555;
  --charcoal:#1e1e1e;
  --line:#cfcfcf;
  --white:#fff;
  --footer-green:#3fae44;
}
*{box-sizing:border-box;margin:0;padding:0}
html,body{width:1200px;height:4021px;overflow:hidden;background:var(--white)}
body{font-family:"Merriweather",Georgia,serif;color:var(--ink)}
.canvas{position:relative;width:1200px;height:4021px;overflow:hidden}
.abs{position:absolute}
.btn{position:absolute;display:flex;align-items:center;justify-content:center;font-size:11px;border-radius:3px}
.btn-solid{background:var(--green);color:var(--white);font-weight:700}
.btn-outline{border:1px solid #888;color:var(--ink);background:var(--white)}
.btn-ghost{border:1px solid #bbb;color:var(--white)}
.btn-line{border:1.5px solid var(--green);color:var(--green);font-weight:700;background:var(--white)}

/* header */
.brand{position:absolute;display:flex;align-items:center;gap:8px;font-weight:900;color:var(--green);font-size:17px}
.brand-dot{width:34px;height:34px;border-radius:50%;background:var(--green)}
.nav{position:absolute;top:64px;right:99px;display:flex;gap:31px;font-size:12px;color:var(--ink)}
.phone{position:absolute;top:26px;left:889px;font-size:12px;display:flex;align-items:center;gap:6px}

/* hero */
.hero-photo{position:absolute;left:0;top:97px;width:1200px;height:520px;background:linear-gradient(100deg,#c9d98a 0%,#8fbf4a 30%,#5d9a2d 60%,#2f6e1c 100%)}
.hero-title{position:absolute;top:228px;left:0;width:1200px;text-align:center;font-size:46px;font-weight:700;color:var(--green-dark);line-height:45px}
.hero-sub{position:absolute;top:333px;left:0;width:1200px;text-align:center;font-size:17px;color:#1b1b1b}

/* service cards */
.card{position:absolute;top:702px;width:321px;height:339px;background:var(--white);border-radius:8px;box-shadow:0 2px 10px rgba(0,0,0,.12);overflow:hidden;text-align:center}
.card-photo{height:168px}
.card h3{margin-top:28px;font-size:18px;color:var(--green);font-weight:700}
.card p{margin:12px auto 0;width:250px;font-size:12px;line-height:17px;color:#333}
.card .btn{left:105px;top:278px;width:111px;height:28px}

/* benefits band */
.band{position:absolute;left:0;top:1115px;width:1200px;height:412px;background:radial-gradient(ellipse at 50% 40%,#1c6a30 0%,#0f4a21 70%,#0a3a18 100%)}
.band-title{position:absolute;top:1168px;width:1200px;text-align:center;font-size:29px;font-weight:700;color:var(--white)}
.band-title span{color:#7fd16a}
.bubble{position:absolute;width:132px;height:132px;border-radius:50%;background:var(--green);color:var(--white);display:flex;flex-direction:column;align-items:center;justify-content:center;text-align:center;font-size:13px;line-height:17px}
.bubble svg{margin-bottom:8px}
.bubble::after{content:"";position:absolute;right:-14px;bottom:26px;border-left:22px solid var(--green);border-top:12px solid transparent;border-bottom:12px solid transparent;transform:rotate(30deg)}
.bubble.last::after{display:none}

/* about */
.about-photo{position:absolute;left:0;top:1527px;width:760px;height:381px;background:linear-gradient(90deg,#8a8a8a 0%,#5a5a5a 55%,#1f1f1f 100%)}
.about-bg{position:absolute;left:687px;top:1527px;width:513px;height:381px;background:var(--charcoal)}
.about h2{position:absolute;left:712px;top:1593px;font-size:29px;color:var(--green-light);font-weight:700}
.about .lead{position:absolute;left:712px;top:1655px;width:360px;font-size:13px;font-weight:700;color:var(--white);line-height:20px}
.about .body{position:absolute;left:712px;top:1715px;width:370px;font-size:13px;color:#e4e4e4;line-height:20px}

/* inquiry */
.map{position:absolute;left:97px;top:1983px;width:491px;height:366px;background:linear-gradient(135deg,#e8efe2,#cfdcc9 60%,#a8c6e0)}
.inquiry-title{position:absolute;left:632px;top:1978px;font-size:29px;font-weight:700;color:var(--green)}
.field{position:absolute;height:34px;border:1px solid var(--line);border-radius:3px;display:flex;align-items:center;gap:8px;padding-left:14px;font-size:11px;color:#777}
.check{position:absolute;display:flex;align-items:center;gap:10px;font-size:11px;color:#555}
.box{width:14px;height:14px;border:1px solid #bbb;border-radius:2px;display:flex;align-items:center;justify-content:center}
.box.on{background:var(--green);border-color:var(--green)}

/* cta */
.cta{position:absolute;left:0;top:2424px;width:1200px;height:261px;background:linear-gradient(180deg,#2a2a2a,#1c1c1c)}
.cta-text{position:absolute;top:2494px;width:1200px;text-align:center;font-size:22px;color:var(--white);line-height:31px}

/* process */
.process{position:absolute;left:0;top:2685px;width:1200px;height:526px;background:linear-gradient(180deg,#1f6e2e,#165a26)}
.process-title{position:absolute;top:2752px;width:1200px;text-align:center;font-size:29px;font-weight:700;color:#f3c94a}
.step{position:absolute;width:128px;height:128px;border-radius:50%;display:flex;flex-direction:column;align-items:center;justify-content:center;text-align:center;color:var(--white);font-size:13px;line-height:16px}
.step svg{margin-bottom:8px}
.step.light{background:var(--green-light)}
.step.dark{background:#1e8a37}
.step::after{content:"";position:absolute;right:-14px;top:52px;border-left:16px solid;border-top:12px solid transparent;border-bottom:12px solid transparent}
.step.light::after{border-left-color:var(--green-light)}
.step.dark::after{border-left-color:#1e8a37}
.step.end::after{display:none}

/* clients */
.clients-title{position:absolute;top:3282px;width:1200px;text-align:center;font-size:29px;font-weight:700;color:var(--green)}
.client{position:absolute;top:3366px;width:150px;display:flex;align-items:center;justify-content:center;gap:8px;font-size:14px;font-weight:700;color:#2b2b2b;height:50px}
.client i{width:18px;height:18px;border-radius:50%;background:#2b2b2b;flex:none}

/* footer */
.footer-bg{position:absolute;left:0;top:3501px;width:1200px;height:520px;background:linear-gradient(180deg,#242424,#171717)}
.footer-heading{position:absolute;font-size:16px;font-weight:400;color:var(--footer-green);line-height:20px}
.footer-text{position:absolute;font-size:12px;color:#eee;line-height:15px}
.links a{display:block;color:#eee;text-decoration:none;font-size:12px;line-height:15px;margin-bottom:12px}
.badge{position:absolute;background:#3a3a3a;border-radius:6px}
.copy{position:absolute;left:97px;top:3968px;font-size:11px;color:#ddd}
.social{position:absolute;top:3967px;width:14px;height:14px;border-radius:50%;background:#777}
</style>
</head>
<body>
<div class="canvas">

  <header>
    <div class="brand" style="left:97px;top:32px"><span class="brand-dot"></span>7 Bright Harbor</div>
    <div class="btn btn-line" style="left:724px;top:19px;width:75px;height:28px">Drop Off</div>
    <div class="btn btn-line" style="left:811px;top:19px;width:60px;height:28px">Pick Up</div>
    <div class="phone">
      <svg width="12" height="12" viewBox="0 0 24 24"><path fill="#111" d="M6.6 10.8a15 15 0 0 0 6.6 6.6l2.2-2.2c.3-.3.7-.4 1-.2 1.1.4 2.3.6 3.6.6.6 0 1 .4 1 1V20c0 .6-.4 1-1 1A17 17 0 0 1 3 4c0-.6.4-1 1-1h3.5c.6 0 1 .4 1 1 0 1.3.2 2.5.6 3.6.1.3 0 .7-.2 1z"/></svg>
      (555) 201-4480
    </div>
    <div class="btn btn-solid" style="left:1008px;top:18px;width:93px;height:29px;gap:6px">
      <svg width="12" height="12" viewBox="0 0 24 24" fill="none" stroke="#fff" stroke-width="2"><path d="M4 4h16v11H9l-5 4z"/></svg>Live Chat
    </div>
    <nav class="nav">
      <span>IT Asset Disposition</span><span>Electronics Recycling</span><span>Secure Data Destruction</span><span>Product Destruction</span><span>About</span><span>Contact Us</span>
    </nav>
  </header>

  <section class="hero">
    <div class="hero-photo" role="img" aria-label="Photo of hands passing a glass globe with a small tree over a soft green meadow"></div>
    <svg class="abs" style="left:0;top:470px" width="1200" height="160" viewBox="0 0 1200 160" preserveAspectRatio="none">
      <path d="M0 70 C180 160 330 150 520 110 C720 60 900 30 1200 70 L1200 160 L0 160Z" fill="#dfeccf"/>
      <path d="M0 110 C200 170 380 160 560 130 C760 95 950 80 1200 110 L1200 160 L0 160Z" fill="#ffffff"/>
    </svg>
    <h1 class="hero-title">Certified E-Recycling<br>Made Easy.</h1>
    <p class="hero-sub">Reuse &amp; Recycle 99.9% of all materials we receive.</p>
    <div class="btn btn-solid" style="left:521px;top:389px;width:158px;height:32px;font-size:12px">Items We Recycle</div>
  </section>

  <section class="services">
    <article class="card" style="left:97px">
      <div class="card-photo" role="img" aria-label="Photo of green recycling bins lined along a street" style="background:linear-gradient(180deg,#6b8c4e,#2f4a2c)"></div>
      <h3>BIN Program</h3>
      <p>Fill up our Bin at Your Location, when done, we come and pick up!</p>
      <div class="btn btn-outline">READ MORE</div>
    </article>
    <article class="card" style="left:440px">
      <div class="card-photo" role="img" aria-label="Photo of a teal container filled with discarded electronics" style="background:linear-gradient(180deg,#8aa0a0,#2c8c8a)"></div>
      <h3>Same Day Pickups Available</h3>
      <p>Secure Chain of Custody</p>
      <div class="btn btn-outline">READ MORE</div>
    </article>
    <article class="card" style="left:782px">
      <div class="card-photo" role="img" aria-label="Photo of a heap of shredded computer drives and parts" style="background:linear-gradient(180deg,#6f6a5e,#2b2824)"></div>
      <h3>On-site Data Destruction</h3>
      <p>Lorem Ipsum is simply dummy text of the printing and typesetting...</p>
      <div class="btn btn-solid">READ MORE</div>
    </article>
  </section>

  <section>
    <div class="band" role="img" aria-label="Dark green background with a faint circuit board texture"></div>
    <h2 class="band-title">Save time. <span>Save money.</span> Save the planet.</h2>
    <div class="bubble" style="left:181px;top:1245px">
      <svg width="34" height="34" viewBox="0 0 24 24" fill="none" stroke="#fff" stroke-width="1.4"><circle cx="14" cy="13" r="7"/><path d="M14 9v4l3 2M2 10h5M3 13h4M2 16h5"/></svg>Quick<br>Response</div>
    <div class="bubble" style="left:360px;top:1328px">
      <svg width="30" height="30" viewBox="0 0 24 24" fill="none" stroke="#fff" stroke-width="1.4"><rect x="3" y="5" width="18" height="16" rx="2"/><path d="M3 10h18M8 3v4M16 3v4M7 14h2M11 14h2M15 14h2M7 17h2M11 17h2"/></svg>Immediate<br>Scheduling</div>
    <div class="bubble" style="left:535px;top:1242px">
      <svg width="38" height="30" viewBox="0 0 28 22" fill="none" stroke="#fff" stroke-width="1.4"><path d="M2 4h15v12H2zM17 8h5l4 4v4h-9"/><circle cx="7" cy="18" r="2"/><circle cx="21" cy="18" r="2"/><circle cx="9" cy="9" r="3"/></svg>On-time Secure<br>Pickup</div>
    <div class="bubble" style="left:711px;top:1328px">
      <svg width="32" height="32" viewBox="0 0 24 24" fill="none" stroke="#fff" stroke-width="1.4"><path d="M12 3l3 5H9zM5 12l-2 5h6M19 12l2 5h-6M9 8l-4 4M15 8l4 4M9 17h6"/></svg>Certified Recy-<br>cling Process</div>
    <div class="bubble last" style="left:889px;top:1245px">
      <svg width="34" height="30" viewBox="0 0 28 24" fill="none" stroke="#fff" stroke-width="1.4"><circle cx="6" cy="5" r="3"/><path d="M2 12c0-3 8-3 8 0M20 4a4 4 0 0 1 4 4c0 3-4 7-4 7s-4-4-4-7a4 4 0 0 1 4-4zM4 20h18"/></svg>Certifications &amp;<br>Asset Tracking<br>Delivered</div>
  </section>

  <section class="about">
    <div class="about-photo" role="img" aria-label="Black and white photo of two workers sorting electronic equipment in a warehouse"></div>
    <div class="about-bg"></div>
    <h2>About Us</h2>
    <p class="lead">We are here for our community. We help the community by offering free drop-off</p>
    <p class="body">To put it simply: if there is a cord attached, we can recycle it. From computers to photocopiers to washers and dryers, and far far more… we'll help you.</p>
    <div class="btn btn-solid" style="left:708px;top:1806px;width:103px;height:28px">ABOUT US</div>
    <div class="btn btn-ghost" style="left:821px;top:1806px;width:145px;height:28px">ITEMS WE RECYCLE</div>
  </section>

  <section class="inquiry">
    <div class="map" role="img" aria-label="Street map showing the drop-off location with a red pin"></div>
    <h2 class="inquiry-title">Quick Inquiry</h2>
    <div class="field" style="left:632px;top:2042px;width:228px">
      <svg width="11" height="11" viewBox="0 0 24 24" fill="none" stroke="#1f8c3b" stroke-width="2"><circle cx="12" cy="8" r="4"/><path d="M4 21c0-5 16-5 16 0"/></svg>First Name</div>
    <div class="field" style="left:875px;top:2042px;width:226px">
      <svg width="11" height="11" viewBox="0 0 24 24" fill="none" stroke="#1f8c3b" stroke-width="2"><circle cx="12" cy="8" r="4"/><path d="M4 21c0-5 16-5 16 0"/></svg>Last Name</div>
    <div class="field" style="left:632px;top:2089px;width:228px">
      <svg width="11" height="11" viewBox="0 0 24 24" fill="none" stroke="#1f8c3b" stroke-width="2"><rect x="7" y="2" width="10" height="20" rx="2"/></svg>Phone</div>
    <div class="field" style="left:875px;top:2089px;width:226px">
      <svg width="12" height="11" viewBox="0 0 24 24" fill="none" stroke="#1f8c3b" stroke-width="2"><rect x="2" y="5" width="20" height="14"/><path d="M2 5l10 8 10-8"/></svg>Email</div>
    <div class="check" style="left:648px;top:2144px"><span class="box"></span>Electronics Recycling</div>
    <div class="check" style="left:648px;top:2169px"><span class="box"></span>Equipment &amp; Product Destruction</div>
    <div class="check" style="left:902px;top:2144px"><span class="box on"><svg width="10" height="10" viewBox="0 0 24 24" fill="none" stroke="#fff" stroke-width="3"><path d="M4 12l5 5L20 6"/></svg></span>Secure Data Destruction</div>
    <div class="check" style="left:902px;top:2169px"><span class="box"></span>IT Asset Destruction</div>
    <div class="field" style="left:632px;top:2202px;width:469px;height:82px;align-items:flex-start;padding-top:12px">
      <svg width="11" height="11" viewBox="0 0 24 24" fill="none" stroke="#1f8c3b" stroke-width="2"><path d="M4 4h16v12H8l-4 4z"/></svg>Message:</div>
    <div class="btn btn-solid" style="left:633px;top:2307px;width:196px;height:34px;font-size:13px;font-weight:400">Submit</div>
  </section>

  <section>
    <div class="cta" role="img" aria-label="Dark background with a faint texture of stacked electronics"></div>
    <p class="cta-text">Save time and disposal costs.<br>We pick up loads of E-Waste over 500 Ibs for free!</p>
    <div class="btn btn-solid" style="left:445px;top:2583px;width:145px;height:27px;font-weight:400">ITEMS WE RECYCLE</div>
    <div class="btn btn-ghost" style="left:604px;top:2583px;width:153px;height:27px">SCHEDULE A PICKUP</div>
  </section>

  <section>
    <div class="process"></div>
    <h2 class="process-title">Our Process</h2>
    <div class="step dark" style="left:156px;top:2918px"><svg width="30" height="30" viewBox="0 0 24 24" fill="none" stroke="#fff" stroke-width="1.4"><rect x="4" y="7" width="11" height="13"/><path d="M8 7V3h12v13h-5"/></svg>On-site<br>Collection</div>
    <div class="step light" style="left:281px;top:2918px"><svg width="34" height="28" viewBox="0 0 28 22" fill="none" stroke="#fff" stroke-width="1.4"><path d="M2 4h15v12H2zM17 8h5l4 4v4h-9"/><circle cx="7" cy="18" r="2"/><circle cx="21" cy="18" r="2"/></svg>Secure<br>Transport</div>
    <div class="step dark end" style="left:406px;top:2918px"><svg width="30" height="28" viewBox="0 0 24 24" fill="none" stroke="#fff" stroke-width="1.4"><path d="M10 5h11M10 12h11M10 19h11M3 5l3 3M3 12h4M3 19l3-3"/></svg>Sorting</div>

    <div class="step light" style="left:534px;top:2821px"><svg width="32" height="28" viewBox="0 0 24 24" fill="none" stroke="#fff" stroke-width="1.4"><rect x="8" y="5" width="8" height="14"/><path d="M5 7c-2 3-2 7 0 10M3 5c-3 4-3 10 0 14M19 7c2 3 2 7 0 10M21 5c3 4 3 10 0 14"/></svg>Databearing<br>Devices</div>
    <div class="step dark" style="left:658px;top:2821px"><svg width="28" height="30" viewBox="0 0 24 24" fill="none" stroke="#fff" stroke-width="1.4"><rect x="4" y="3" width="16" height="10"/><path d="M6 16v5M10 16v5M14 16v5M18 16v5"/></svg>Data<br>Destruction</div>
    <div class="step light" style="left:782px;top:2821px"><svg width="30" height="30" viewBox="0 0 24 24" fill="none" stroke="#fff" stroke-width="1.4"><circle cx="12" cy="12" r="9"/><path d="M7 10l5-3 5 3v5l-5 3-5-3z"/></svg>Refurbish</div>
    <div class="step dark end" style="left:908px;top:2821px"><svg width="30" height="30" viewBox="0 0 24 24" fill="none" stroke="#fff" stroke-width="1.4"><circle cx="12" cy="12" r="10"/><path d="M6 8h2l2 7h7l1-5H9"/><circle cx="11" cy="17.5" r="1"/><circle cx="16" cy="17.5" r="1"/></svg>Remarket</div>

    <div class="step light" style="left:545px;top:3003px"><svg width="32" height="28" viewBox="0 0 24 24" fill="none" stroke="#fff" stroke-width="1.4"><rect x="8" y="5" width="8" height="14"/><path d="M5 7c-2 3-2 7 0 10M19 7c2 3 2 7 0 10"/></svg>Non-data-Bear-<br>ing Devices</div>
    <div class="step dark" style="left:669px;top:3003px"><svg width="30" height="30" viewBox="0 0 24 24" fill="none" stroke="#fff" stroke-width="1.4"><path d="M3 21l9-9M10 4l10 10-3 3L7 7z"/></svg>Dismantle &amp;<br>process</div>
    <div class="step light" style="left:794px;top:3003px"><svg width="30" height="30" viewBox="0 0 24 24" fill="none" stroke="#fff" stroke-width="1.4"><path d="M12 3l3 5H9zM5 12l-2 5h6M19 12l2 5h-6M9 8l-4 4M15 8l4 4M9 17h6"/></svg>Recycle</div>
    <div class="step dark end" style="left:919px;top:3003px"><svg width="26" height="30" viewBox="0 0 24 24" fill="none" stroke="#fff" stroke-width="1.4"><path d="M5 2h10l4 4v16H5zM8 10h8M8 14h8M8 18h5"/></svg>Reporting</div>
  </section>

  <section>
    <h2 class="clients-title">Our Clients</h2>
    <svg class="abs" style="left:96px;top:3382px" width="10" height="16" viewBox="0 0 10 16"><path d="M8 2L2 8l6 6" fill="none" stroke="#bbb" stroke-width="2"/></svg>
    <svg class="abs" style="left:1095px;top:3382px" width="10" height="16" viewBox="0 0 10 16"><path d="M2 2l6 6-6 6" fill="none" stroke="#1f8c3b" stroke-width="2"/></svg>
    <div class="client" style="left:123px"><i></i>Cedar Bean</div>
    <div class="client" style="left:267px">Ridgeline Sports</div>
    <div class="client" style="left:415px">Halvorsen Inns</div>
    <div class="client" style="left:584px;font-size:18px">Northwave</div>
    <div class="client" style="left:768px">Alder Grove Chapel</div>
    <div class="client" style="left:924px"><i></i>Sound Harbor</div>
  </section>

  <footer>
    <div class="footer-bg" role="img" aria-label="Dark footer background with a faint photo texture"></div>
    <div class="brand" style="left:97px;top:3636px;font-size:16px"><span class="brand-dot" style="width:28px;height:28px"></span>7 Bright Harbor</div>

    <h4 class="footer-heading" style="left:300px;top:3572px">Our Mission</h4>
    <p class="footer-text" style="left:300px;top:3604px;width:238px">We are a socially conscious recycling company that's fully committed to helping community, including small &amp; large business, with a one-stop solution for the responsible disposal of E-Waste.</p>
    <p class="footer-text" style="left:300px;top:3697px;width:238px">Local and Sustainable<br>0% waste<br>0% landfill<br>100% Environmental Conscious!</p>

    <h4 class="footer-heading" style="left:612px;top:3572px">Quick Links</h4>
    <div class="abs links" style="left:612px;top:3605px"><a>Home</a><a style="text-decoration:underline">How It Works</a><a>Environment</a><a>Community</a><a>About</a></div>
    <div class="abs links" style="left:749px;top:3605px"><a>FAQs</a><a>Blog</a><a>Contact</a><a>Request a Pickup</a></div>

    <h4 class="footer-heading" style="left:930px;top:3572px">Contact Info</h4>
    <svg class="abs" style="left:930px;top:3608px" width="14" height="18" viewBox="0 0 24 30"><path d="M12 2a9 9 0 0 1 9 9c0 7-9 17-9 17S3 18 3 11a9 9 0 0 1 9-9z" fill="none" stroke="#3fae44" stroke-width="2"/><circle cx="12" cy="11" r="3" fill="none" stroke="#3fae44" stroke-width="2"/></svg>
    <p class="footer-text" style="left:963px;top:3607px;line-height:19px">214 Larkspur Way North<br>Suite B<br>Kentwood, WA 98000<br>USA</p>
    <svg class="abs" style="left:930px;top:3698px" width="14" height="14" viewBox="0 0 24 24"><path fill="none" stroke="#3fae44" stroke-width="2" d="M6.6 10.8a15 15 0 0 0 6.6 6.6l2.2-2.2c.3-.3.7-.4 1-.2 1.1.4 2.3.6 3.6.6.6 0 1 .4 1 1V20c0 .6-.4 1-1 1A17 17 0 0 1 3 4c0-.6.4-1 1-1h3.5c.6 0 1 .4 1 1 0 1.3.2 2.5.6 3.6.1.3 0 .7-.2 1z"/></svg>
    <p class="footer-text" style="left:963px;top:3699px;line-height:21px">(555) 201-4480<br>(555) 310-7720</p>

    <div class="badge" style="left:261px;top:3856px;width:59px;height:85px;border-radius:50%"></div>
    <div class="badge" style="left:401px;top:3869px;width:134px;height:60px;border-radius:30px"></div>
    <div class="badge" style="left:609px;top:3866px;width:165px;height:64px"></div>
    <div class="badge" style="left:848px;top:3856px;width:93px;height:72px;background:#e07a1f"></div>

    <p class="copy">Copyright © 2021 7 Bright Harbor, LLC. All Rights Reserved</p>
    <span class="social" style="left:1015px"></span>
    <span class="social" style="left:1051px"></span>
    <span class="social" style="left:1087px;background:#3fae44"></span>
  </footer>

</div>
</body>
</html>
```